Startup photography business has a new logo, now we need business cards

Design a business card for the two partners of our business.
Our business Brisk Pelican has a new logo and we need to design a business card to showcase it and us.
Our colours of blue and orange are punchy and vivid, but how can we make the most of it on our card?

It should have our name Brisk Pelican
name of partner
phone number
email
website

Industry/Entity Type

Professional Photography

Contact Information for Business Card

Tom Ashworth
+61 400 55 61 72
tom@briskpelican.com.au
briskpelican.com.au

second card
Neil Porter
+61 400 918 263
neil@briskpelican.com.au
briskpelican.com.au

Colors
f37122
f68d4c
33a6d7
0592cd

Requirements
Must have
• one version of our logo, we have included options
• Name
• phone number
• email
• website
Nice to have
• instagram briskpelicanmedia
• twitter briskpelicanmedia
• facebook briskpelicanmedia

```html
<!DOCTYPE html>
<html lang="en">
<head>
<meta charset="utf-8">
<title>Brisk Pelican — Business Cards</title>
<link rel="stylesheet" href="https://fonts.googleapis.com/css2?family=Stardos+Stencil:wght@700&family=PT+Sans+Narrow:wght@400;700&display=swap">
<style>
  :root {
    --backdrop: #e4e1dc;
    --card: #ede3d5;
    --band: #6cbbe2;
    --orange: #f37122;
    --ink: #111111;
    --contact-ink: #1d1d1d;
    --icon-bg: #f4f6f8;
    --icon-ink: #2a2a2a;
  }
  * { margin: 0; padding: 0; box-sizing: border-box; }
  html, body {
    width: 1200px;
    height: 1012px;
    overflow: hidden;
    background: var(--backdrop);
  }
  .stage { position: relative; width: 1200px; height: 1012px; }

  .card {
    position: absolute;
    width: 722px;
    height: 430px;
    background: var(--card);
    box-shadow: 0 2px 8px rgba(0,0,0,0.12);
  }
  .card--tom { left: 101px; top: 72px; }
  .card--neil { left: 311px; top: 533px; }

  .brand {
    position: absolute;
    left: 0;
    top: 30px;
    width: 720px;
    display: flex;
    flex-direction: column;
    align-items: center;
    transform: translateX(-0px);
  }
  .brand {
    left: 260px;
    width: 200px;
  }
  .brand__mark {
    width: 100px;
    height: 100px;
    border-radius: 50%;
    background: var(--orange);
  }
  .brand__name {
    margin-top: 10px;
    font-family: "PT Sans Narrow", sans-serif;
    font-weight: 700;
    font-size: 33px;
    letter-spacing: 0.5px;
    color: var(--orange);
    text-transform: uppercase;
    white-space: nowrap;
  }

  .person {
    position: absolute;
    top: 212px;
    font-family: "Stardos Stencil", serif;
    font-weight: 700;
    font-size: 68px;
    line-height: 1;
    color: var(--ink);
    letter-spacing: 1px;
    white-space: nowrap;
  }
  .card--tom .person { left: 136px; }
  .card--neil .person { left: 183px; }

  .contact-band {
    position: absolute;
    left: 0;
    bottom: 0;
    width: 100%;
    height: 82px;
    background: var(--band);
  }
  .contact {
    position: absolute;
    top: 50%;
    transform: translateY(-50%);
    display: flex;
    align-items: center;
    gap: 10px;
    font-family: "PT Sans Narrow", sans-serif;
    font-size: 22px;
    color: var(--contact-ink);
    white-space: nowrap;
  }
  .contact__icon {
    width: 34px;
    height: 34px;
    border-radius: 50%;
    background: var(--icon-bg);
    box-shadow: inset 0 -2px 3px rgba(0,0,0,0.15);
    display: flex;
    align-items: center;
    justify-content: center;
  }
  .contact__icon svg { width: 18px; height: 18px; }

  .card--tom .contact--phone { left: 24px; }
  .card--tom .contact--email { left: 240px; }
  .card--tom .contact--web { left: 517px; }
  .card--neil .contact--phone { left: 28px; }
  .card--neil .contact--email { left: 242px; }
  .card--neil .contact--web { left: 519px; }
</style>
</head>
<body>
<main class="stage">

  <article class="card card--tom">
    <header class="brand">
      <div class="brand__mark"></div>
      <div class="brand__name">Brisk Pelican</div>
    </header>
    <h1 class="person">Tom Ashworth</h1>
    <footer class="contact-band">
      <span class="contact contact--phone">
        <span class="contact__icon">
          <svg viewBox="0 0 18 18"><rect x="5" y="1.5" width="8" height="15" rx="1.5" fill="var(--icon-ink)"/><rect x="6.5" y="3.5" width="5" height="5" fill="var(--icon-bg)"/></svg>
        </span>+61 400 55 61 72
      </span>
      <span class="contact contact--email">
        <span class="contact__icon">
          <svg viewBox="0 0 18 18"><rect x="2" y="4" width="14" height="10" fill="none" stroke="var(--icon-ink)" stroke-width="1.6"/><path d="M2 4 L9 10 L16 4" fill="none" stroke="var(--icon-ink)" stroke-width="1.6"/></svg>
        </span>tom@briskpelican.com.au
      </span>
      <span class="contact contact--web">
        <span class="contact__icon">
          <svg viewBox="0 0 18 18"><circle cx="9" cy="9" r="6.5" fill="none" stroke="var(--icon-ink)" stroke-width="1.5"/><ellipse cx="9" cy="9" rx="3" ry="6.5" fill="none" stroke="var(--icon-ink)" stroke-width="1.2"/><path d="M2.5 9 H15.5" stroke="var(--icon-ink)" stroke-width="1.2"/></svg>
        </span>briskpelican.com.au
      </span>
    </footer>
  </article>

  <article class="card card--neil">
    <header class="brand">
      <div class="brand__mark"></div>
      <div class="brand__name">Brisk Pelican</div>
    </header>
    <h1 class="person">Neil Porter</h1>
    <footer class="contact-band">
      <span class="contact contact--phone">
        <span class="contact__icon">
          <svg viewBox="0 0 18 18"><rect x="5" y="1.5" width="8" height="15" rx="1.5" fill="var(--icon-ink)"/><rect x="6.5" y="3.5" width="5" height="5" fill="var(--icon-bg)"/></svg>
        </span>+61 400 918 263
      </span>
      <span class="contact contact--email">
        <span class="contact__icon">
          <svg viewBox="0 0 18 18"><rect x="2" y="4" width="14" height="10" fill="none" stroke="var(--icon-ink)" stroke-width="1.6"/><path d="M2 4 L9 10 L16 4" fill="none" stroke="var(--icon-ink)" stroke-width="1.6"/></svg>
        </span>neil@briskpelican.com.au
      </span>
      <span class="contact contact--web">
        <span class="contact__icon">
          <svg viewBox="0 0 18 18"><circle cx="9" cy="9" r="6.5" fill="none" stroke="var(--icon-ink)" stroke-width="1.5"/><ellipse cx="9" cy="9" rx="3" ry="6.5" fill="none" stroke="var(--icon-ink)" stroke-width="1.2"/><path d="M2.5 9 H15.5" stroke="var(--icon-ink)" stroke-width="1.2"/></svg>
        </span>briskpelican.com.au
      </span>
    </footer>
  </article>

</main>
</body>
</html>
```